BRC Business cards

We are a medium sized property company based in London and require a logo, Business card which reflects a professional company and incorporates our catchy name.

Our statement is (Building for the future) we like colours such as royal blue, greens and light browns but will look at anything.

Contact Information for Business Card

Brookcrest Estates Limited
Unit 4, 15-17 Farrowby Lane
London
SE22 7QN

Web: www.brookcrestestates-example.com

Email: brookcrestltd@mailbox-example.com

Telephone: +44-208-555-0142
Fax: +44-208-555-0187

```html
<!DOCTYPE html>
<html lang="en">
<head>
<meta charset="utf-8">
<title>Brookcrest Estates Limited – Business Card</title>
<link rel="stylesheet" href="https://fonts.googleapis.com/css2?family=Ubuntu:wght@400;500;700&display=swap">
<style>
  :root {
    --navy: #0f2d6e;
    --green: #5cb82a;
    --ink: #3a3a3a;
    --card: #ffffff;
    --backdrop: #6f7c88;
  }
  * { box-sizing: border-box; margin: 0; padding: 0; }
  html, body {
    width: 1200px; height: 1000px; overflow: hidden;
    background: var(--backdrop);
    font-family: "Ubuntu", sans-serif;
  }
  .card {
    position: absolute; left: 100px; top: 214px;
    width: 1000px; height: 572px;
    background: var(--card);
    box-shadow: 0 14px 34px rgba(0,0,0,0.35);
    overflow: hidden;
  }
  .brand {
    position: absolute; right: 70px; top: 62px;
    display: flex; align-items: center; gap: 14px;
  }
  .brand-mark { width: 22px; height: 22px; background: var(--green); }
  .brand-name {
    color: var(--navy); font-weight: 700; font-size: 30px; line-height: 1.05;
    width: 210px;
  }
  .rule {
    position: absolute; left: 240px; right: 0; top: 222px;
    height: 3px; background: var(--navy);
  }
  .holder { position: absolute; left: 70px; top: 170px; }
  .holder-name { color: var(--navy); font-weight: 700; font-size: 34px; }
  .holder-role { color: var(--ink); font-size: 26px; margin-top: 2px; }
  .address {
    position: absolute; left: 70px; top: 320px;
    color: var(--ink); font-size: 27px; line-height: 1.3;
  }
  .contacts {
    position: absolute; left: 590px; top: 250px;
    color: var(--ink); font-size: 22px; line-height: 1.55;
    list-style: none;
  }
  .contacts .label { display: inline-block; width: 34px; }
  .side-tab {
    position: absolute; left: 0; top: 300px;
    width: 30px; height: 30px; background: var(--green);
  }
  .band-green {
    position: absolute; left: 0; bottom: 0;
    width: 590px; height: 20px; background: var(--green);
  }
  .band-navy {
    position: absolute; left: 590px; right: 0; bottom: 0;
    height: 26px; background: var(--navy);
  }
</style>
</head>
<body>
  <div class="card">
    <div class="brand">
      <span class="brand-mark"></span>
      <span class="brand-name">Brookcrest Estates Limited</span>
    </div>

    <div class="holder">
      <div class="holder-name">Card Holder Name</div>
      <div class="holder-role">Designation</div>
    </div>
    <div class="rule"></div>

    <div class="side-tab"></div>

    <address class="address" style="font-style:normal">
      Unit 4, 15-17 Farrowby Lane<br>
      London SE22 7QN
    </address>

    <ul class="contacts">
      <li><span class="label">p :</span>+44-208-555-0142</li>
      <li><span class="label">f :</span>+44-208-555-0187</li>
      <li><span class="label">e :</span>brookcrestltd@mailbox-example.com</li>
      <li><span class="label">w :</span>www.brookcrestestates-example.com</li>
    </ul>

    <div class="band-green"></div>
    <div class="band-navy"></div>
  </div>
</body>
</html>
```